Help me create an amazing cover for my first ebook!!

I am looking to have a modern and professional looking cover for my first ebook. It will be published through Borvex Quill Self Press and will need to follow their formatting and guidelines. I want the cover to have a modern and vibrant feel, that appeals to a millennial audience. This is a real estate book that is focused on a niche category catered to young professionals, so the idea would be to appeal to them.

Title:
The Twentysomething Playbook for Duplex Living

A Smart Property Buying Plan to Start Early, Cut Your Housing Costs (Sometimes to Zero), and Speed Up Your Path to Lasting Wealth.

Davin Osterlund

Target Market(s)

Real Estate investors, investors, millennials, young professionals, college educated, 20-40 years old.Financial freedom, finance.

Industry/Entity Type

Real Estate

Font styles to use
Sans Serif

Colors

Designer to choose colors to be used in the design.

Requirements
Must have
• Must follow the borvex quill self press format. I attached a screenshot of the details, it can also be found here: https://qsp.borvexbooks.example/en_US/help/topic/R481736025
• Must include this title:
• The Twentysomething Playbook for Duplex Living
• A Smart Property Buying Plan to Start Early, Cut Your Housing Costs (Sometimes to Zero), and Speed Up Your Path to Lasting Wealth.
• Davin Osterlund.
• I added examples of book covers I like to use as a guide, I also added some color pallette examples.
Nice to have
• Modern, clean design that's not too busy. Some sort of simple photo or illustration to incorporate in the cover along with the text would be nice.

```html
<!DOCTYPE html>
<html lang="en">
<head>
<meta charset="utf-8">
<title>The Twentysomething Playbook for Duplex Living — Davin Osterlund</title>
<link rel="stylesheet" href="https://fonts.googleapis.com/css2?family=Montserrat:wght@500;600;700;800&display=swap">
<style>
  :root {
    --slate: #435459;
    --teal: #8dd3d6;
    --lime: #c6d63f;
    --orange: #e27418;
    --white: #ffffff;
    --mist: #dfeaec;
  }
  html, body {
    margin: 0;
    padding: 0;
    width: 750px;
    height: 1200px;
    overflow: hidden;
    background: var(--slate);
  }
  .cover {
    position: relative;
    width: 750px;
    height: 1200px;
    background: var(--slate);
    font-family: "Montserrat", sans-serif;
    overflow: hidden;
  }
  .cover-art {
    position: absolute;
    inset: 0;
    width: 750px;
    height: 1200px;
  }
  .author {
    position: absolute;
    top: 60px;
    left: 0;
    width: 750px;
    text-align: center;
    margin: 0;
    font-weight: 500;
    font-size: 24px;
    letter-spacing: 5px;
    color: var(--teal);
    text-transform: uppercase;
  }
  .title {
    position: absolute;
    top: 612px;
    left: 0;
    width: 750px;
    margin: 0;
    text-align: center;
    text-transform: uppercase;
  }
  .title-lead {
    display: block;
    font-weight: 700;
    font-size: 49px;
    line-height: 56px;
    color: var(--teal);
    letter-spacing: 0.5px;
  }
  .title-main {
    display: block;
    font-weight: 800;
    font-size: 108px;
    line-height: 124px;
    color: var(--lime);
    letter-spacing: -2px;
  }
  .title-joiner {
    display: flex;
    align-items: center;
    justify-content: center;
    gap: 22px;
    width: 596px;
    margin: 0 auto;
    font-weight: 700;
    font-size: 30px;
    line-height: 36px;
    color: var(--white);
    text-transform: none;
  }
  .title-joiner::before,
  .title-joiner::after {
    content: "";
    flex: 1;
    height: 4px;
    background: var(--orange);
  }
  .title-tail {
    display: block;
    width: 596px;
    margin: 0 auto;
    padding-bottom: 10px;
    border-bottom: 4px solid var(--orange);
    font-weight: 700;
    font-size: 64px;
    line-height: 70px;
    color: var(--white);
  }
  .subtitle {
    position: absolute;
    top: 956px;
    left: 0;
    width: 750px;
    margin: 0;
    text-align: center;
    font-weight: 500;
    font-size: 27px;
    line-height: 37.5px;
    letter-spacing: 0.3px;
    color: var(--mist);
    text-transform: uppercase;
  }
</style>
</head>
<body>
  <main class="cover">
    <svg class="cover-art" viewBox="0 0 750 1200" xmlns="http://www.w3.org/2000/svg">
      <defs>
        <linearGradient id="photo-tones" x1="0" y1="0" x2="0" y2="1">
          <stop offset="0" stop-color="#e9f0f1"/>
          <stop offset="0.22" stop-color="#c9d6d6"/>
          <stop offset="0.42" stop-color="#efe7d8"/>
          <stop offset="0.6" stop-color="#c9ad82"/>
          <stop offset="0.72" stop-color="#d9cbb4"/>
          <stop offset="0.86" stop-color="#5f9ea6"/>
          <stop offset="1" stop-color="#3f7b80"/>
        </linearGradient>
      </defs>
      <rect class="hero-photo" x="0" y="40" width="750" height="560" fill="url(#photo-tones)"
            role="img" aria-label="Photo of a white Spanish-style villa at dusk with a lit covered patio, palm trees and a curved swimming pool"/>
      <polygon class="band-top" fill="var(--slate)" points="0,0 750,0 750,56 212,206 110,96 0,96"/>
      <polygon class="band-bottom" fill="var(--slate)" points="0,348 204,588 750,448 750,1200 0,1200"/>
    </svg>

    <p class="author">Davin Osterlund</p>

    <h1 class="title">
      <span class="title-lead">The Twentysomething</span>
      <span class="title-main">Playbook</span>
      <span class="title-joiner">for</span>
      <span class="title-tail">Duplex Living</span>
    </h1>

    <p class="subtitle">
      A Smart Property Buying Plan<br>
      to Start Early, Cut Your<br>
      Housing Costs (Sometimes to Zero),<br>
      and Speed Up Your Path<br>
      to Lasting Wealth.
    </p>
  </main>
</body>
</html>
```